Business card design needed for Renewable utilities company based in New Zealand.

We supply and install solar panels and all components along with it for a fully customisable PV system that helps customer save money on their energy bills right away and also save the planet!

I have attached logo & website design files to give you a better insight.

Industry/Entity Type

Business

```html
<!DOCTYPE html>
<html lang="en">
<head>
<meta charset="utf-8">
<title>Clear Sky Power – Business Card</title>
<link rel="stylesheet" href="https://fonts.googleapis.com/css2?family=Questrial&family=Roboto+Condensed:wght@400;700&display=swap">
<style>
  :root {
    --navy-light: #23508a;
    --navy: #143a74;
    --navy-deep: #0c2456;
    --panel-grey: #d6d4d4;
    --bar-grey: #aea6a6;
    --band-grey: #6e6e6e;
    --ink: #4d4b4b;
    --ink-strong: #5a5858;
    --tagline: #c9c9c9;
    --white: #ffffff;
    --faint: rgba(190, 200, 220, 0.75);
    --icon-blue: #2f5a8c;
  }
  * { box-sizing: border-box; margin: 0; padding: 0; }
  html, body { width: 1200px; height: 1000px; overflow: hidden; background: var(--white); }
  body { position: relative; font-family: "Roboto Condensed", "Arial Narrow", sans-serif; }

  .card { position: absolute; left: 209px; width: 782px; height: 470px; overflow: hidden; }
  .card--front { top: 20px; }
  .card--back { top: 511px; }

  .navy-field {
    position: absolute; left: 0; right: 0;
    background: radial-gradient(ellipse 70% 90% at 22% 18%, var(--navy-light) 0%, var(--navy) 45%, var(--navy-deep) 100%);
  }
  .card--front .navy-field { top: 0; height: 212px; }
  .card--back .navy-field { top: 0; bottom: 0; }

  .brand { position: absolute; top: 56px; left: 0; right: 0; text-align: center; color: var(--white); }
  .brand__mark { display: block; margin: 0 auto 14px; width: 78px; height: 78px; border-radius: 50%; background: var(--white); }
  .brand__name { font-family: "Questrial", "Century Gothic", sans-serif; font-size: 33px; letter-spacing: 0.5px; }

  .info-strip { position: absolute; top: 212px; left: 0; right: 0; height: 186px; background: var(--panel-grey); }
  .solar-surface {
    position: absolute; top: 0; left: 281px; right: 0; bottom: 0;
    background: linear-gradient(180deg, #d9d7d7, #cfcccc);
  }

  .social-list { position: absolute; top: 24px; left: 0; width: 274px; list-style: none; }
  .social-list li {
    position: relative; height: 30px; margin-bottom: 23px;
    background: var(--bar-grey); color: var(--ink);
    font-size: 21px; line-height: 30px; padding-left: 110px;
  }
  .social-list li::before {
    content: ""; position: absolute; left: 50px; top: -6px;
    width: 40px; height: 40px; border-radius: 50%; background: var(--icon-blue);
  }

  .holder { position: absolute; top: 74px; left: 298px; font-size: 27px; color: var(--ink-strong); white-space: nowrap; }
  .holder__name { font-weight: 700; letter-spacing: 1px; }
  .holder__email { font-weight: 400; }

  .tagline-band {
    position: absolute; top: 398px; left: 0; right: 0; height: 72px;
    background: var(--band-grey); color: var(--tagline);
    font-size: 25px; text-align: center; padding-top: 6px; letter-spacing: 0.5px;
  }

  .back-emblem {
    position: absolute; left: 273px; top: 121px; width: 232px; height: 232px;
    border-radius: 50%; background: rgba(110, 140, 190, 0.18);
  }
  .contact { position: absolute; top: 176px; left: 0; right: 0; text-align: center; color: var(--faint); }
  .contact__web { font-size: 32px; letter-spacing: 0.5px; margin-bottom: 8px; }
  .contact__line { font-size: 23px; display: flex; align-items: center; justify-content: center; gap: 8px; margin-bottom: 6px; }
  .contact__line svg { fill: var(--faint); }
</style>
</head>
<body>
  <section class="card card--front">
    <div class="navy-field"></div>
    <div class="brand">
      <span class="brand__mark"></span>
      <div class="brand__name">Clear Sky Power</div>
    </div>
    <div class="info-strip">
      <div class="solar-surface" role="img" aria-label="Grid of solar panel cells in light grey"></div>
      <ul class="social-list">
        <li>/clearskypower</li>
        <li>@clearskypower</li>
        <li>/clearskypower</li>
      </ul>
      <p class="holder"><span class="holder__name">Mara Quill</span> / <span class="holder__email">mara@clearskypower.com</span></p>
    </div>
    <div class="tagline-band">¡Save money and also save the planet!</div>
  </section>

  <section class="card card--back">
    <div class="navy-field"></div>
    <div class="back-emblem"></div>
    <div class="contact">
      <p class="contact__web">www.clearskypower.com</p>
      <p class="contact__line">
        <svg width="24" height="26" viewBox="0 0 24 26" aria-hidden="true"><path d="M5 1c1.5-.6 2.6 0 3.2 1.3l1.6 3.6c.5 1.1.2 2-.7 2.7l-1.6 1.2c.9 2.6 3 5.1 5.5 6.6l1.4-1.4c.8-.8 1.8-.9 2.8-.3l3.3 2c1.2.8 1.5 1.9.8 3.2l-1 1.8c-.8 1.4-2.3 2-4 1.6C8.6 21.6 2.6 14.4 1.4 6.6 1.2 4.7 2 3.2 3.5 2.2z"/></svg>
        0800.555.0199
      </p>
      <p class="contact__line">
        <svg width="32" height="26" viewBox="0 0 32 26" aria-hidden="true"><path d="M2 10l14-9 14 9v15H2z" fill="none" stroke="rgba(190,200,220,0.75)" stroke-width="1.6"/><path d="M2 10l14 9 14-9" fill="none" stroke="rgba(190,200,220,0.75)" stroke-width="1.6"/><circle cx="16" cy="9" r="3.2" fill="none" stroke="rgba(190,200,220,0.75)" stroke-width="1.4"/></svg>
        info@clearskypower.com
      </p>
    </div>
  </section>
</body>
</html>
```